A Maple Syrup Label for a Local Buniness

We are looking for a label for our maple syrup business. Our business currently sells honey, and we are expanding into maple syrup. Our Business name is "Brackley Honey" and we currently have a logo attached below. We would like to incorporate the bee and BH part, but the label could also read "Brackley Farms" with the words maple syrup. We do not want consumers to confuse the maple syrup jars with the honey jars. It should be clear that the jars contain maple syrup. We are open to new designs as well.

```html
<!DOCTYPE html>
<html lang="en">
<head>
<meta charset="utf-8">
<title>Brackley Farm Maple Syrup Label</title>
<link rel="stylesheet" href="https://fonts.googleapis.com/css2?family=Alegreya:wght@400;700;800&family=Alegreya+Sans:wght@700;800&display=swap">
<style>
  :root {
    --page: #ffffff;
    --label: #0b0c0b;
    --gold: #c4944a;
    --caption: #111111;
  }
  * { margin: 0; padding: 0; box-sizing: border-box; }
  html, body { width: 1200px; height: 945px; overflow: hidden; background: var(--page); }
  .sheet { position: relative; width: 1200px; height: 945px; }

  .label {
    position: absolute; top: 111px; width: 486px; height: 717px;
    background: var(--label); color: var(--gold);
  }
  .label--front { left: 100px; }
  .label--back { left: 616px; }

  .frame-outer {
    position: absolute; left: 29px; top: 30px; width: 433px; height: 658px;
    border: 2px solid var(--gold);
  }
  .frame-inner {
    position: absolute; left: 34px; top: 35px; width: 423px; height: 648px;
    border: 1px solid var(--gold);
  }

  .ornament {
    position: absolute; width: 96px; height: 86px;
    background: radial-gradient(ellipse at var(--o, 0% 0%), rgba(196,148,74,.55), rgba(196,148,74,.12) 55%, rgba(196,148,74,0) 80%);
  }
  .ornament--tl { --o: 0% 0%; }
  .ornament--tr { --o: 100% 0%; }
  .ornament--bl { --o: 0% 100%; }
  .ornament--br { --o: 100% 100%; }
  .label--front .ornament--tl { left: 39px; top: 39px; }
  .label--front .ornament--tr { right: 39px; top: 39px; }
  .label--front .ornament--bl { left: 39px; bottom: 39px; }
  .label--front .ornament--br { right: 39px; bottom: 39px; }
  .label--back .ornament--tl { left: 39px; top: 39px; }
  .label--back .ornament--tr { right: 36px; top: 39px; }
  .label--back .ornament--bl { left: 39px; bottom: 39px; }
  .label--back .ornament--br { right: 36px; bottom: 39px; }

  .brand-title {
    position: absolute; left: 0; right: 0; top: 80px; text-align: center;
    font-family: "Alegreya", serif; font-weight: 800;
    font-size: 64px; line-height: 57px; letter-spacing: 1px;
  }
  .brand-title span { display: block; }

  .hero-art {
    position: absolute; left: 124px; top: 217px; width: 237px; height: 280px;
    border-radius: 48% 48% 50% 50% / 40% 40% 60% 60%;
    background: radial-gradient(ellipse at 50% 65%, #b38642 0%, #6f4f22 55%, rgba(40,30,15,0) 78%);
  }

  .product-name {
    position: absolute; left: 0; right: 0; top: 528px; text-align: center;
    font-family: "Alegreya Sans", sans-serif; font-weight: 800;
    font-size: 50px; line-height: 50px; letter-spacing: .5px;
  }
  .volume {
    position: absolute; left: 0; right: 0; top: 607px; text-align: center;
    font-family: "Alegreya Sans", sans-serif; font-weight: 700;
    font-size: 37px; line-height: 38px;
  }

  .story { position: absolute; left: 70px; top: 142px; width: 380px; }
  .story-heading {
    font-family: "Alegreya", serif; font-weight: 700;
    font-size: 24px; line-height: 30px; white-space: nowrap;
  }
  .story-body {
    margin-top: 28px;
    font-family: "Alegreya", serif; font-weight: 400;
    font-size: 24px; line-height: 29.2px; letter-spacing: .2px; white-space: nowrap;
  }
  .story-signature {
    margin-top: 34px;
    font-family: "Alegreya", serif; font-weight: 700;
    font-size: 24px; line-height: 30px;
  }

  .brand-name {
    position: absolute; left: 0; right: 0; top: 575px; text-align: center;
    font-family: "Alegreya", serif; font-weight: 700;
    font-size: 24px; line-height: 30px; color: var(--gold);
  }

  .caption {
    position: absolute; top: 849px; width: 486px; text-align: center;
    font-family: Arial, Helvetica, sans-serif; font-size: 16px; color: var(--caption);
  }
  .caption--front { left: 100px; }
  .caption--back { left: 616px; }
</style>
</head>
<body>
<main class="sheet">

  <section class="label label--front" aria-label="Front label">
    <div class="frame-outer"></div>
    <div class="frame-inner"></div>
    <div class="ornament ornament--tl" role="img" aria-label="Gold filigree corner ornament"></div>
    <div class="ornament ornament--tr" role="img" aria-label="Gold filigree corner ornament"></div>
    <div class="ornament ornament--bl" role="img" aria-label="Gold filigree corner ornament"></div>
    <div class="ornament ornament--br" role="img" aria-label="Gold filigree corner ornament"></div>

    <h1 class="brand-title"><span>BRACKLEY</span><span>FARM</span></h1>

    <div class="hero-art" role="img" aria-label="Engraved-style gold illustration of a bee above an oval vignette of a barn, tree and fence"></div>

    <p class="product-name">MAPLE SYRUP</p>
    <p class="volume">12 FL OZ</p>
  </section>

  <section class="label label--back" aria-label="Back label">
    <div class="ornament ornament--tl" role="img" aria-label="Gold filigree corner ornament"></div>
    <div class="ornament ornament--tr" role="img" aria-label="Gold filigree corner ornament"></div>
    <div class="ornament ornament--bl" role="img" aria-label="Gold filigree corner ornament"></div>
    <div class="ornament ornament--br" role="img" aria-label="Gold filigree corner ornament"></div>

    <article class="story">
      <h2 class="story-heading">From Tree to Table — With Love</h2>
      <p class="story-body">Tapped from the maples on our<br>Ontario farm, our pure maple<br>syrup is hand-crafted by the<br>Brackley family using time-<br>honored methods. Every bottle<br>supports sustainable practices<br>and generations of family<br>farming.</p>
      <p class="story-signature">– Brackley Farms</p>
    </article>

    <p class="brand-name">Brackley Honey</p>
  </section>

  <p class="caption caption--front">Maple Syrup Label Front-Side</p>
  <p class="caption caption--back">Maple Syrup Label Back-Side Text (Suggested)</p>

</main>
</body>
</html>
```